Fast Money - Simple Book Cover Design

Hello,

I am in need of a cover for my new book. The Book Title Is

"Standing Growth - Keys to Glowing Customer Ratings That Fill The Calendar and Draw Fresh Clients Through Every Entrance!"

Author: Fireman Dale Orsworth

What I want: This is a book for businesses on improving their online reputation. I want to have 5 Stars on the cover. You can look at this quarvex search for ideas of what I am meaning.....

(copy and paste)

http://www.quarvex-find.example/search?q=5+star+online+reviews&mode=images&ref=kx7Lp2QwZt9 (copy and paste)

I am open to different color schemes for the book. I am partial to dark blues if you make it look good. Here is another book that I really like the cover of....

http://www.brindlemart.example/Clipwave-Tactics-Earning-Promotion-ebook/item/Z93KT4WQPX

I want the cover BOLD and to STAND OUT.

I am looking for a design to help establish me as an authority for online reputation marketing. This book will be both in Pagely format and be used in print as well.

I am open to questions....

Thanks!

Dale

Reason: I don't believe we have received the right designs. I am going to give everyone more time...

Reason: Hi everyone, I had some stuff come up and was not able to be involved in this project. I am extending because we have not seen the exact thing we want and need time to work with designers to get it right. Thanks Dale

Reason: I am currently traveling and can't wrap this up until I get back.

Target Market(s)

Business Owners

Industry/Entity Type

Business

Requirements
Must have
• Title and Subtitle

Author Name

5 Stars Images....
Nice to have
• Creativity

Bold and stand out

Professional

Should not have
• thin text, small to read text, lame graphics,

```html
<!DOCTYPE html>
<html lang="en">
<head>
<meta charset="utf-8">
<title>Standing Growth – Book Cover</title>
<link rel="stylesheet" href="https://fonts.googleapis.com/css2?family=Arimo:wght@700&display=swap">
<style>
  :root {
    --cover-red: #e3000c;
    --cover-red-deep: #b5000a;
    --cover-red-light: #ff5a5a;
    --text-white: #ffffff;
    --star-gold-light: #fff4b0;
    --star-gold: #f0c93a;
    --star-gold-dark: #b88a12;
  }
  html, body {
    margin: 0;
    padding: 0;
    overflow: hidden;
    background: var(--cover-red);
  }
  .cover {
    position: relative;
    width: 900px;
    height: 1200px;
    overflow: hidden;
    background: var(--cover-red);
    font-family: "Arimo", Arial, sans-serif;
    font-weight: 700;
    color: var(--text-white);
  }
  .cover-texture {
    position: absolute;
    inset: 0;
    background:
      radial-gradient(ellipse 48% 30% at 50% 52%, rgba(255,255,255,0.55) 0%, rgba(255,180,180,0.25) 35%, rgba(255,0,0,0) 75%),
      linear-gradient(180deg, var(--cover-red) 0%, var(--cover-red-light) 24%, #f03a3a 50%, var(--cover-red-light) 73%, var(--cover-red) 76%, var(--cover-red-deep) 100%);
  }
  .star-row {
    position: absolute;
    inset: 0;
  }
  .star {
    position: absolute;
    width: 100px;
    height: 96px;
    transform: translate(-50%, -50%);
    filter: drop-shadow(0 2px 3px rgba(90,0,0,0.45));
  }
  .series-title {
    position: absolute;
    top: 448px;
    left: 0;
    width: 100%;
    margin: 0;
    text-align: center;
    font-size: 38px;
    text-decoration: underline;
    text-underline-offset: 6px;
    text-decoration-thickness: 3px;
    text-shadow: 0 1px 3px rgba(90,0,0,0.5);
  }
  .subtitle {
    position: absolute;
    top: 540px;
    left: 50px;
    width: 800px;
    margin: 0;
    text-align: center;
    font-size: 44px;
    line-height: 58px;
    text-shadow: 0 1px 3px rgba(90,0,0,0.5);
  }
  .author {
    position: absolute;
    top: 902px;
    left: 0;
    width: 100%;
    margin: 0;
    text-align: center;
    font-size: 37px;
    text-shadow: 0 1px 3px rgba(90,0,0,0.5);
  }
</style>
</head>
<body>
<main class="cover">
  <div class="cover-texture" role="img" aria-label="Red background with a glossy dotted bubble texture"></div>

  <svg width="0" height="0" style="position:absolute">
    <defs>
      <radialGradient id="gold-fill" cx="50%" cy="40%" r="60%">
        <stop offset="0%" stop-color="var(--star-gold-light)"/>
        <stop offset="55%" stop-color="var(--star-gold)"/>
        <stop offset="100%" stop-color="var(--star-gold-dark)"/>
      </radialGradient>
      <symbol id="gold-star" viewBox="0 0 100 96">
        <polygon points="50,2 61.8,36 97.5,36.5 69,58 79.4,92.5 50,72 20.6,92.5 31,58 2.5,36.5 38.2,36"
                 fill="url(#gold-fill)" stroke="var(--star-gold-dark)" stroke-width="1.5" stroke-linejoin="round"/>
        <polygon points="50,2 50,52 61.8,36" fill="#ffffff" opacity="0.25"/>
        <polygon points="50,52 79.4,92.5 69,58" fill="#7a5a00" opacity="0.18"/>
        <polygon points="50,52 2.5,36.5 31,58" fill="#7a5a00" opacity="0.12"/>
      </symbol>
    </defs>
  </svg>

  <div class="star-row" aria-label="Five stars">
    <svg class="star" style="left:450px; top:219px"><use href="#gold-star"/></svg>
    <svg class="star" style="left:229px; top:281px"><use href="#gold-star"/></svg>
    <svg class="star" style="left:672px; top:281px"><use href="#gold-star"/></svg>
    <svg class="star" style="left:100px; top:456px"><use href="#gold-star"/></svg>
    <svg class="star" style="left:800px; top:456px"><use href="#gold-star"/></svg>
  </div>

  <h1 class="series-title">Standing Growth</h1>
  <p class="subtitle">Keys to Glowing Customer Ratings That Fill the Calendar and Draw Fresh Clients Through Every Entrance!</p>
  <p class="author">by Fireman Dale Orsworth</p>
</main>
</body>
</html>
```